Business Card Design

Our Motto is "Protecting Australia's Underground Utilities"

We want the Southern Cross inside a shield I have attached the southern cross and our old shield design

Product description is: Vacuum Excavation & Utility Location
Wet & Dry Vacuum Loading
Confined Space Entry Specialists
High Pressure Cleaning

The Southern Cross in the shield must be blue and white. The Company name must be Coastal Pipeguard Services. The Green & Gold Shield logo I uploaded is my OLD logo design. Thank you

Target Market(s)

Civil Construction

Industry/Entity Type

Business

Contact Information for Business Card

Coastal Pipeguard Services Pty Ltd
Corey Halbrook(Director)
0413862975
coreyh@pipeguardco.com.au
A.B.N.52938470116

Colors
0456a3

Requirements
Must have
• Southern Cross inside a shield, Blue and white design on the Southern Cross shield.
Must say Coastal Pipeguard Services P/L

```html
<!DOCTYPE html>
<html lang="en">
<head>
<meta charset="utf-8">
<title>Coastal Pipeguard Services – Business Card</title>
<link rel="stylesheet" href="https://fonts.googleapis.com/css2?family=Arimo:wght@400;700&display=swap">
<style>
  :root {
    --backdrop: #ececec;
    --card: #ffffff;
    --green: #006837;
    --green-text: #0b6a33;
    --gold: #f4d000;
    --white: #ffffff;
  }
  * { margin: 0; padding: 0; box-sizing: border-box; }
  html, body { width: 1200px; height: 750px; overflow: hidden; }
  body {
    background: var(--backdrop);
    font-family: "Arimo", Arial, sans-serif;
    color: var(--green-text);
    position: relative;
  }
  .card {
    position: absolute;
    top: 217px;
    width: 493px;
    height: 283px;
    background: var(--card);
    border-radius: 14px;
    overflow: hidden;
  }
  .card--front { left: 91px; }
  .card--back { left: 620px; }
  .card__wave { position: absolute; inset: 0; width: 100%; height: 100%; }

  .brand-name {
    position: absolute;
    color: var(--green);
    font-weight: 700;
    line-height: 1.15;
    text-transform: uppercase;
  }
  .card--front .brand-name { left: 32px; top: 44px; width: 96px; font-size: 13px; }
  .card--back .brand-name { left: 322px; top: 200px; width: 74px; font-size: 10.5px; }

  .person {
    position: absolute;
    right: 19px;
    top: 30px;
    text-align: right;
    color: var(--white);
  }
  .person__name { font-size: 15px; }
  .person__role { font-size: 11px; margin-top: 1px; }

  .contact {
    position: absolute;
    left: 34px;
    top: 185px;
    font-size: 11.5px;
  }
  .contact__heading { font-weight: 700; font-size: 12px; margin-bottom: 3px; }
  .contact__line { display: flex; align-items: center; height: 14.7px; }
  .contact__icon { width: 12px; height: 10px; margin-right: 5px; flex: none; }
  .contact__line--plain { padding-left: 17px; }

  .address {
    position: absolute;
    left: 270px;
    top: 215px;
    font-size: 11.5px;
    line-height: 15px;
  }

  .products {
    position: absolute;
    left: 42px;
    top: 97px;
  }
  .products__title { font-size: 19px; margin-bottom: 20px; }
  .products__list { list-style: none; font-size: 13.5px; }
  .products__item {
    position: relative;
    padding-left: 24px;
    height: 20.5px;
    line-height: 20.5px;
  }
  .products__item::before {
    content: "";
    position: absolute;
    left: 3px;
    top: 5px;
    width: 10px;
    height: 10px;
    border-radius: 50%;
    background: var(--green);
  }
</style>
</head>
<body>

<section class="card card--front">
  <svg class="card__wave" viewBox="0 0 493 283" aria-hidden="true">
    <path d="M312,0 C345,60 338,125 378,172 C418,218 432,245 432,283 L493,283 L493,0 Z" fill="var(--green)"/>
    <path d="M332,0 C355,55 355,120 395,170 C432,215 447,245 447,283" fill="none" stroke="var(--white)" stroke-width="9"/>
    <path d="M332,0 C355,55 355,120 395,170 C432,215 447,245 447,283" fill="none" stroke="var(--gold)" stroke-width="4.5"/>
  </svg>

  <p class="brand-name">Coastal Pipeguard Services</p>

  <div class="person">
    <p class="person__name">Corey Halbrook</p>
    <p class="person__role">Director</p>
  </div>

  <div class="contact">
    <p class="contact__heading">Contact</p>
    <p class="contact__line">
      <svg class="contact__icon" viewBox="0 0 12 10" aria-hidden="true"><path d="M1,3 Q6,-1 11,3 L10,4.5 L8,4 L7.5,3 L4.5,3 L4,4 L2,4.5 Z M2.5,5 L9.5,5 L10.5,9.5 L1.5,9.5 Z" fill="var(--green)"/></svg>
      0413862975
    </p>
    <p class="contact__line">
      <svg class="contact__icon" viewBox="0 0 12 10" aria-hidden="true"><rect x="0.5" y="1" width="11" height="8" fill="var(--green)"/><path d="M1,1.5 L6,5.5 L11,1.5 M1,8.5 L4.5,4.5 M11,8.5 L7.5,4.5" fill="none" stroke="var(--white)" stroke-width="1"/></svg>
      coreyh@pipeguardco.com.au
    </p>
    <p class="contact__line">
      <svg class="contact__icon" viewBox="0 0 12 10" aria-hidden="true"><rect x="1" y="0.8" width="10" height="6.6" fill="none" stroke="var(--green)" stroke-width="1.4"/><rect x="4" y="8" width="4" height="1.6" fill="var(--green)"/></svg>
      www.pipeguardco.com.au
    </p>
    <p class="contact__line contact__line--plain">A.B.N.52938470116</p>
  </div>

  <p class="address">Here your Address<br>Home or Office</p>
</section>

<section class="card card--back">
  <svg class="card__wave" viewBox="0 0 493 283" aria-hidden="true">
    <path d="M311,0 C328,80 350,140 392,182 C432,218 446,252 444,283 L493,283 L493,0 Z" fill="var(--green)"/>
  </svg>

  <div class="products">
    <h2 class="products__title" style="font-weight:400">Product Description</h2>
    <ul class="products__list">
      <li class="products__item">Vacuum Excavation &amp; Utility Location</li>
      <li class="products__item">Wet &amp; Dry Vacuum Loading</li>
      <li class="products__item">Confined Space Entry Specialists</li>
      <li class="products__item">High Pressure Cleaning</li>
    </ul>
  </div>

  <p class="brand-name">Coastal Pipeguard Services</p>
</section>

</body>
</html>
```